International Trading Company, 'VOLA' needs a Business Card

The company name is "VOLA" and it has own logo design.
I'd like to use its logo on this business card.
I need two side Business Card.
I'll look forward to your great design.
Thank you very much in advance.

Contact Information for Business Card

Company Name : Vola Harbor Limited
Information Example
Tobias Wrenfold
Mobile(use icon please) : 1 (555) 014-2290
Tel(use icon please) : 1 (555) 014-6835
Email(use icon please) : tobias27@volaharbor.example
Address(use icon please) : 482 Larkmoor Rd, New York, NY 10199, USA

```html
<!DOCTYPE html>
<html lang="en">
<head>
<meta charset="utf-8">
<title>Vola Harbor Limited – Business Card</title>
<link rel="stylesheet" href="https://fonts.googleapis.com/css2?family=Open+Sans:wght@400;600;700&display=swap">
<style>
  :root {
    --canvas-bg: #e6e4e1;
    --card-white: #ffffff;
    --card-mist: #e4e4e6;
    --brand-blue: #3d52b8;
    --brand-blue-deep: #26368f;
    --brand-blue-light: #6579cf;
    --logo-grey: #8c8c8e;
    --text-grey: #6d6d72;
    --icon-blue: #5a8fd0;
    --rule-blue: #2c3a9e;
  }
  * { box-sizing: border-box; margin: 0; padding: 0; }
  html, body { width: 1200px; height: 1023px; overflow: hidden; }
  body {
    background: var(--canvas-bg);
    font-family: "Open Sans", Arial, sans-serif;
    display: flex;
    flex-direction: column;
    align-items: center;
    justify-content: center;
    gap: 44px;
  }
  .card {
    position: relative;
    width: 760px;
    height: 434px;
    border-radius: 22px;
    overflow: hidden;
    box-shadow: 0 6px 18px rgba(0,0,0,0.18);
  }

  /* Front */
  .card--front {
    background: radial-gradient(ellipse at 45% 45%, var(--card-white) 30%, var(--card-mist) 100%);
  }
  .front__logo {
    position: absolute;
    right: 56px;
    top: 28px;
    font-size: 150px;
    font-weight: 700;
    letter-spacing: 4px;
    line-height: 1;
    color: var(--logo-grey);
  }
  .front__rule {
    position: absolute;
    left: 280px;
    right: 0;
    top: 238px;
    height: 2px;
    background: var(--rule-blue);
  }
  .front__name-tab {
    position: absolute;
    left: 0;
    top: 238px;
    width: 290px;
    height: 46px;
    background: linear-gradient(90deg, var(--brand-blue-deep), var(--brand-blue-light));
    border-top-right-radius: 30px;
    display: flex;
    align-items: center;
    padding-left: 40px;
  }
  .front__name {
    color: #fff;
    font-size: 23px;
    font-weight: 600;
    letter-spacing: 0.5px;
  }
  .contact-list {
    position: absolute;
    left: 40px;
    top: 300px;
    list-style: none;
    display: flex;
    flex-direction: column;
    gap: 9px;
  }
  .contact-list li,
  .front__address {
    display: flex;
    align-items: center;
    gap: 12px;
    font-size: 14px;
    color: var(--text-grey);
  }
  .contact-icon { width: 20px; height: 20px; flex: none; }
  .front__address {
    position: absolute;
    right: 30px;
    bottom: 30px;
  }

  /* Back */
  .card--back {
    background: radial-gradient(ellipse at 50% 50%, var(--brand-blue-light) 0%, var(--brand-blue) 50%, var(--brand-blue-deep) 100%);
    display: flex;
    align-items: center;
    justify-content: center;
  }
  .back__logo {
    font-size: 190px;
    font-weight: 700;
    letter-spacing: 6px;
    color: #fff;
    line-height: 1;
  }
</style>
</head>
<body>

<section class="card card--front" aria-label="Card front">
  <div class="front__logo">VOLA</div>
  <div class="front__rule"></div>
  <div class="front__name-tab"><span class="front__name">Tobias Wrenfold</span></div>

  <ul class="contact-list">
    <li>
      <svg class="contact-icon" viewBox="0 0 20 20" aria-hidden="true">
        <circle cx="10" cy="10" r="9" fill="none" stroke="var(--icon-blue)" stroke-width="1.4"/>
        <path d="M7 5.5c-1 .6-1.4 1.6-.8 3 .8 2 2.4 3.8 4.4 4.8 1.3.6 2.3.3 3-.7l-1.8-1.4-1 .8c-1-.5-1.9-1.4-2.4-2.5l.8-1z" fill="var(--icon-blue)"/>
      </svg>
      1 (555) 014-2290
    </li>
    <li>
      <svg class="contact-icon" viewBox="0 0 20 20" aria-hidden="true">
        <circle cx="10" cy="10" r="9" fill="var(--icon-blue)"/>
        <rect x="7" y="5" width="6" height="10" rx="1" fill="#fff"/>
        <rect x="8" y="6.3" width="4" height="6" fill="var(--icon-blue)"/>
      </svg>
      1 (555) 014-6835
    </li>
    <li>
      <svg class="contact-icon" viewBox="0 0 20 20" aria-hidden="true">
        <circle cx="10" cy="10" r="9" fill="none" stroke="var(--icon-blue)" stroke-width="1.4"/>
        <rect x="5.5" y="6.5" width="9" height="7" fill="none" stroke="var(--icon-blue)" stroke-width="1.2"/>
        <path d="M5.5 6.5l4.5 4 4.5-4" fill="none" stroke="var(--icon-blue)" stroke-width="1.2"/>
      </svg>
      tobias27@volaharbor.example
    </li>
    <li>
      <svg class="contact-icon" viewBox="0 0 20 20" aria-hidden="true">
        <circle cx="10" cy="10" r="9" fill="var(--icon-blue)"/>
        <circle cx="10" cy="10" r="5" fill="none" stroke="#fff" stroke-width="1.2"/>
        <path d="M5 10h10M10 5c-2 2.5-2 7.5 0 10M10 5c2 2.5 2 7.5 0 10" fill="none" stroke="#fff" stroke-width="1"/>
      </svg>
      www.volaharbor.example
    </li>
  </ul>

  <div class="front__address">
    482 Larkmoor Rd, New York, NY 10199, USA
    <svg class="contact-icon" viewBox="0 0 20 20" aria-hidden="true">
      <circle cx="10" cy="10" r="9" fill="var(--icon-blue)"/>
      <path d="M10 4.5a3.5 3.5 0 0 0-3.5 3.5c0 2.6 3.5 7 3.5 7s3.5-4.4 3.5-7A3.5 3.5 0 0 0 10 4.5z" fill="#fff"/>
      <circle cx="10" cy="8" r="1.3" fill="var(--icon-blue)"/>
    </svg>
  </div>
</section>

<section class="card card--back" aria-label="Card back">
  <div class="back__logo">VOLA</div>
</section>

</body>
</html>
```